Brindle's Business Card

I need some designs for a new business card including the new logo attached. An old example of our business card is also attached to show all the data that should be included on the new design.
**I added some more examples someone had mocked up**

Contact Information for Business Card

Should include all info on other examples uploaded.

```html
<!DOCTYPE html>
<html lang="en">
<head>
<meta charset="utf-8">
<title>Brindle's Business Card</title>
<link href="https://fonts.googleapis.com/css2?family=Montserrat:wght@600;700;800&family=Arimo:wght@400;700&display=swap" rel="stylesheet">
<style>
  :root {
    --bg: #e6e6e6;
    --paper: #ffffff;
    --brand-blue: #0a6fc2;
    --brand-blue-deep: #0862ad;
    --brand-red: #e3202a;
    --ink-grey: #5a5a5a;
    --ghost-grey: #e4e4e4;
    --white: #ffffff;
  }
  * { box-sizing: border-box; margin: 0; padding: 0; }
  html, body {
    width: 1200px; height: 802px; overflow: hidden;
    background: var(--bg);
    font-family: "Arimo", Arial, sans-serif;
  }
  .stage { position: relative; width: 1200px; height: 802px; }
  .card {
    position: absolute; top: 246px;
    width: 540px; height: 309px;
    overflow: hidden;
    box-shadow: 0 6px 18px rgba(0,0,0,0.14);
  }
  /* Front */
  .card-front { left: 40px; background: var(--paper); }
  .front-edge {
    position: absolute; left: 0; right: 0; bottom: 0; height: 8px;
    display: flex;
  }
  .front-edge .edge-red { flex: 0 0 55%; background: var(--brand-red); }
  .front-edge .edge-blue { flex: 1; background: var(--brand-blue); }
  .front-ghost-mark {
    position: absolute; right: -40px; top: -30px;
    width: 300px; height: 300px; border-radius: 50%;
    border: 34px solid var(--ghost-grey);
  }
  .wordmark {
    position: absolute; left: 34px; top: 38px;
    display: flex; align-items: center; gap: 10px;
  }
  .wordmark-dot {
    width: 40px; height: 40px; border-radius: 50%;
    background: var(--brand-blue);
  }
  .wordmark-name {
    font-family: "Montserrat", sans-serif; font-weight: 800;
    font-size: 40px; letter-spacing: 1px; color: var(--brand-blue);
    line-height: 1;
  }
  .wordmark-tag {
    font-family: "Montserrat", sans-serif; font-weight: 700;
    font-size: 9.5px; color: var(--brand-blue); letter-spacing: 0.4px;
    margin-top: 4px;
  }
  .holder-name {
    position: absolute; left: 36px; top: 132px;
    font-family: "Montserrat", sans-serif; font-weight: 700;
    font-size: 26px; color: var(--brand-red); letter-spacing: 0.5px;
  }
  .contact-list {
    position: absolute; left: 36px; top: 196px;
    list-style: none; font-size: 17px; color: var(--ink-grey);
  }
  .contact-list li { display: flex; align-items: center; gap: 10px; margin-bottom: 8px; }
  .contact-list svg { width: 16px; height: 16px; fill: var(--brand-red); }
  .credentials {
    position: absolute; right: 26px; top: 168px; text-align: right;
    font-size: 15px; letter-spacing: 1px; color: var(--ink-grey);
    line-height: 1.5; text-transform: uppercase;
  }
  /* Back */
  .card-back { left: 620px; background: var(--brand-blue); }
  .back-emboss {
    position: absolute; left: -60px; bottom: -90px;
    width: 320px; height: 320px; border-radius: 50%;
    border: 40px solid var(--brand-blue-deep);
    box-shadow: inset 0 2px 4px rgba(255,255,255,0.12);
  }
  .back-title {
    position: absolute; right: 30px; top: 40px; text-align: right; color: var(--white);
  }
  .back-title .name {
    font-family: "Montserrat", sans-serif; font-weight: 800;
    font-size: 56px; letter-spacing: 2px; line-height: 1;
  }
  .back-title .tag {
    font-family: "Montserrat", sans-serif; font-weight: 700;
    font-size: 13px; letter-spacing: 0.6px; margin-top: 6px;
  }
  .service-area {
    position: absolute; right: 30px; top: 160px; text-align: right;
    color: var(--white); font-size: 16px; line-height: 1.35;
  }
  .call-to-action {
    position: absolute; right: 30px; bottom: 28px; text-align: right;
    color: var(--white); font-weight: 700; font-size: 14px;
    line-height: 1.4; text-transform: uppercase;
  }
</style>
</head>
<body>
<main class="stage">
  <section class="card card-front">
    <div class="front-ghost-mark" aria-hidden="true"></div>
    <div class="wordmark">
      <span class="wordmark-dot" aria-hidden="true"></span>
      <div>
        <div class="wordmark-name">BRINDLE'S</div>
        <div class="wordmark-tag">AIR CONDITIONING &amp; HEATING SERVICE</div>
      </div>
    </div>
    <h1 class="holder-name">WYATT BRINDLE</h1>
    <ul class="contact-list">
      <li>
        <svg viewBox="0 0 24 24" aria-hidden="true"><path d="M6.6 10.8a15.1 15.1 0 0 0 6.6 6.6l2.2-2.2a1 1 0 0 1 1-.25 11.4 11.4 0 0 0 3.6.57 1 1 0 0 1 1 1V20a1 1 0 0 1-1 1A17 17 0 0 1 3 4a1 1 0 0 1 1-1h3.5a1 1 0 0 1 1 1c0 1.25.2 2.45.57 3.6a1 1 0 0 1-.25 1z"/></svg>
        555.018.2047
      </li>
      <li>
        <svg viewBox="0 0 24 24" aria-hidden="true"><path d="M2 5h20v14H2z M2 5l10 8 10-8" stroke="#fff" stroke-width="1.5"/></svg>
        hvacbrindle@mailbox.com
      </li>
    </ul>
    <p class="credentials">Licensed &amp; Insured<br>Family Owned &amp; Operated</p>
    <div class="front-edge" aria-hidden="true"><span class="edge-red"></span><span class="edge-blue"></span></div>
  </section>

  <section class="card card-back">
    <div class="back-emboss" aria-hidden="true"></div>
    <div class="back-title">
      <div class="name">BRINDLE'S</div>
      <div class="tag">AIR CONDITIONING &amp; HEATING SERVICE</div>
    </div>
    <p class="service-area">Serves Maple Hollow,<br>IA &amp; Surrounding Areas</p>
    <p class="call-to-action">Call today for all your HVAC,<br>refrigeration &amp; plumbing needs</p>
  </section>
</main>
</body>
</html>
```